PowerPoint Listing Presentation

I am a real estate agent with Branford Oakes Realty in the Las Vegas, Nevada market. I want a power point presentation that I can use with sellers who are considering the sale of their home. This presentation should include the following:
1. Charts and graphs about home sales statistics in the market.
2. Company Logo
3. My photo
4. A graphical description of where buyers come from
5. A graphical description of correct pricing strategies that sell
6. Pages that illustrate the things I do to sell homes.
7. A page that I can change with my personal statistics of annual sales numbers
8. A page that I can change with my personal market statistics as compared to the local association member’s average statistics.
9. Other pages with some graphics, photos and places for me to add data as needed.
Some of my stats:
1. I am a Broker licensed in Nevada since 1987
2. I average over 130 closed home sales per year.
3. I sell my listings in an average of 50 days at 103.52% of list price
4 The average property sells in 63 days at 100.27% of list price.
5. My team is made up of me, an executive assistant, marketing coordinator, buyer specialists, listing specialists

Target Market(s)

Prospective sellers of residential real estate

Industry/Entity Type

Real Estate

Requirements
Nice to have
• Places where I can edit and make changes to graphs, charts and text to make sure the presentation stays consistent with my stats and that of the market.

```html
<!DOCTYPE html>
<html lang="en">
<head>
<meta charset="utf-8">
<title>Reed Branding – Listing Presentation</title>
<link href="https://fonts.googleapis.com/css2?family=Carlito:wght@400;700&display=swap" rel="stylesheet">
<style>
  :root {
    --slide-bg-light: #5a5a5a;
    --slide-bg-dark: #333333;
    --panel-dark: #2b2b2b;
    --band-blue: #2f6fc4;
    --band-blue-light: #5b9be6;
    --swoosh-white: #f4f4f4;
    --title-blue: #9fd0ff;
    --title-edge: #2b5d9a;
    --bullet-text: #f2f2f2;
    --brand-text: #2a2a2a;
    --photo-frame: #ffffff;
    --photo-fill-top: #8a8f96;
    --photo-fill-bottom: #2a2c30;
  }
  * { margin: 0; padding: 0; box-sizing: border-box; }
  html, body {
    width: 1200px; height: 900px; overflow: hidden;
    background: var(--slide-bg-dark);
  }
  .slide {
    position: relative; width: 1200px; height: 900px; overflow: hidden;
    font-family: "Carlito", "Calibri", Arial, sans-serif;
  }
  .slide-backdrop { position: absolute; inset: 0; }
  .agent-photo {
    position: absolute; left: 36px; top: 108px; width: 156px; height: 156px;
    background: var(--photo-frame); padding: 6px;
    box-shadow: 0 0 14px rgba(255,255,255,0.6);
  }
  .agent-photo-fill {
    width: 100%; height: 100%;
    background: linear-gradient(180deg, var(--photo-fill-top), var(--photo-fill-bottom));
  }
  .brand-mark {
    position: absolute; right: 26px; top: 22px;
    display: flex; align-items: center; gap: 8px;
    font-weight: 700; font-size: 22px; color: var(--brand-text);
  }
  .brand-mark-square { width: 16px; height: 16px; background: var(--brand-text); }
  .slide-title {
    position: absolute; left: 333px; top: 118px;
    font-size: 56px; font-weight: 700; color: var(--title-blue);
    -webkit-text-stroke: 1px var(--title-edge);
    text-shadow: 0 0 6px rgba(255,255,255,0.7);
    letter-spacing: 0.5px;
  }
  .stat-list {
    position: absolute; left: 350px; top: 252px; list-style: none;
  }
  .stat-item {
    position: relative; padding-left: 42px;
    font-size: 33px; font-weight: 700; color: var(--bullet-text);
    line-height: 68px;
  }
  .stat-arrow {
    position: absolute; left: 0; top: 24px; width: 22px; height: 22px;
  }
</style>
</head>
<body>
<main class="slide">
  <svg class="slide-backdrop" width="1200" height="900" viewBox="0 0 1200 900" role="img" aria-label="Dark grey background with faint chevron stripes">
    <defs>
      <linearGradient id="bgGrad" x1="0" y1="0" x2="0" y2="1">
        <stop offset="0" stop-color="#4a4a4a"/>
        <stop offset="0.5" stop-color="#5a5a5a"/>
        <stop offset="1" stop-color="#3c3c3c"/>
      </linearGradient>
      <linearGradient id="bandGrad" x1="0" y1="0" x2="1" y2="0">
        <stop offset="0" stop-color="#1f4f96"/>
        <stop offset="0.5" stop-color="#5b9be6"/>
        <stop offset="1" stop-color="#2f6fc4"/>
      </linearGradient>
    </defs>
    <rect width="1200" height="900" fill="url(#bgGrad)"/>
    <!-- left dark panel -->
    <path d="M0 0 H210 C235 250 250 420 225 600 C210 720 190 820 192 900 H0 Z" fill="#2b2b2b"/>
    <!-- blue curved band -->
    <path d="M210 0 H232 C262 250 272 420 248 600 C232 720 212 820 214 900 H192 C190 820 210 720 225 600 C250 420 235 250 210 0 Z" fill="url(#bandGrad)"/>
    <!-- top-right white swoosh -->
    <path d="M700 0 H1200 V118 C1080 40 900 8 700 0 Z" fill="#f4f4f4"/>
    <path d="M700 0 C900 8 1080 40 1200 118 V124 C1080 48 900 14 700 0 Z" fill="#2f6fc4"/>
  </svg>

  <div class="agent-photo">
    <div class="agent-photo-fill" role="img" aria-label="Portrait photo of the agent"></div>
  </div>

  <div class="brand-mark">
    <span class="brand-mark-square"></span>
    <span>Branford Oakes Realty</span>
  </div>

  <h1 class="slide-title">Reed Branding</h1>

  <ul class="stat-list">
    <li class="stat-item"><svg class="stat-arrow" viewBox="0 0 22 22"><path d="M3 3 L19 11 L3 19 L8 11 Z" fill="none" stroke="#f2f2f2" stroke-width="2"/></svg>Broker licenced in Nevada, since 1987</li>
    <li class="stat-item"><svg class="stat-arrow" viewBox="0 0 22 22"><path d="M3 3 L19 11 L3 19 L8 11 Z" fill="none" stroke="#f2f2f2" stroke-width="2"/></svg>Over 130 closed home sales per year</li>
    <li class="stat-item"><svg class="stat-arrow" viewBox="0 0 22 22"><path d="M3 3 L19 11 L3 19 L8 11 Z" fill="none" stroke="#f2f2f2" stroke-width="2"/></svg>Home listing average&nbsp; 50 days</li>
    <li class="stat-item"><svg class="stat-arrow" viewBox="0 0 22 22"><path d="M3 3 L19 11 L3 19 L8 11 Z" fill="none" stroke="#f2f2f2" stroke-width="2"/></svg>Property sales is 63 days</li>
    <li class="stat-item"><svg class="stat-arrow" viewBox="0 0 22 22"><path d="M3 3 L19 11 L3 19 L8 11 Z" fill="none" stroke="#f2f2f2" stroke-width="2"/></svg>103.52 % Price Listing</li>
    <li class="stat-item"><svg class="stat-arrow" viewBox="0 0 22 22"><path d="M3 3 L19 11 L3 19 L8 11 Z" fill="none" stroke="#f2f2f2" stroke-width="2"/></svg>100. 27% Price Sale</li>
  </ul>
</main>
</body>
</html>
```